Velorine Jewellery Display Card

We are a jewellery manufacturer and need artwork for an A4 size strut card to advertise our new "Crescent Loop Pendant "
In the attached files is a picture of the new pendant and artwork for our trademark "Velorine"
We also need to include the phrase " an expression of love "
as part of the artwork.
The background colour should be predominately white

Target Market(s)

This product has been designed as a gift for Mothers as it has their children names
engraved on the pendant

Industry/Entity Type

Manufacturer

Font styles to use
Serif
Script

Colors
ffffff

Requirements
Must have
• Artwork should be simple and elegant , the predominant look in Australian jewellery stores which is where these display cards will be is white, bright and elegant

```html
<!DOCTYPE html>
<html lang="en">
<head>
<meta charset="utf-8">
<title>Velorine – Crescent Loop Pendant</title>
<link href="https://fonts.googleapis.com/css2?family=Tenor+Sans&family=Tinos&family=Great+Vibes&display=swap" rel="stylesheet">
<style>
  :root {
    --paper: #ffffff;
    --brand-grey: #a4b0b4;
    --border-grey: #a9b5b9;
    --heart-grey: #87979c;
    --ink: #111111;
    --silver-light: #eef0f1;
    --silver-dark: #b9c0c3;
  }
  * { margin: 0; padding: 0; box-sizing: border-box; }
  html, body { width: 927px; height: 1200px; overflow: hidden; background: var(--paper); }
  .card { position: relative; width: 927px; height: 1200px; background: var(--paper); }

  .brand-name {
    position: absolute; top: 22px; left: 0; width: 100%;
    text-align: center;
    font-family: "Tenor Sans", sans-serif;
    font-size: 92px; letter-spacing: 2px;
    color: var(--brand-grey);
  }

  .border-row {
    position: absolute; left: 134px; width: 644px;
    display: flex; justify-content: space-between;
    font-family: "Tenor Sans", sans-serif;
    font-size: 27px; color: var(--border-grey);
    line-height: 1;
  }
  .border-row.top { top: 161px; }
  .border-row.bottom { top: 1111px; }

  .border-column {
    position: absolute; top: 232px; height: 800px;
    display: flex; justify-content: space-between;
    writing-mode: vertical-rl;
    font-family: "Tenor Sans", sans-serif;
    font-size: 27px; color: var(--border-grey);
    line-height: 1;
  }
  .border-column.left { left: 74px; transform: rotate(180deg); }
  .border-column.right { left: 818px; }

  .corner-charm {
    position: absolute; width: 72px; height: 84px;
    border-radius: 50% 50% 50% 50% / 55% 55% 45% 45%;
    background: radial-gradient(circle at 45% 40%, var(--silver-light), var(--silver-dark));
  }
  .corner-charm.tl { left: 44px; top: 134px; }
  .corner-charm.tr { left: 790px; top: 134px; }
  .corner-charm.bl { left: 44px; top: 1082px; }
  .corner-charm.br { left: 790px; top: 1082px; }

  .product-title {
    position: absolute; top: 296px; left: 0; width: 100%;
    text-align: center;
    font-family: "Tinos", serif;
    font-size: 23px; color: var(--ink);
  }

  .heart { position: absolute; left: 136px; top: 372px; width: 656px; height: 598px; }
  .heart path { fill: var(--heart-grey); }

  .pendant {
    position: absolute; left: 264px; top: 362px; width: 370px; height: 520px;
  }

  .tagline {
    position: absolute; top: 978px; left: 0; width: 100%;
    text-align: center;
    font-family: "Great Vibes", cursive;
    font-size: 62px; color: var(--ink);
  }
</style>
</head>
<body>
<main class="card">
  <h1 class="brand-name">VELORINE</h1>

  <div class="border-row top"><span>VELORINE</span><span>VELORINE</span><span>VELORINE</span><span>VELORINE</span></div>
  <div class="border-row bottom"><span>VELORINE</span><span>VELORINE</span><span>VELORINE</span><span>VELORINE</span></div>
  <div class="border-column left"><span>VELORINE</span><span>VELORINE</span><span>VELORINE</span><span>VELORINE</span><span>VELORINE</span></div>
  <div class="border-column right"><span>VELORINE</span><span>VELORINE</span><span>VELORINE</span><span>VELORINE</span><span>VELORINE</span></div>

  <div class="corner-charm tl" role="img" aria-label="Small photo of the silver pendant"></div>
  <div class="corner-charm tr" role="img" aria-label="Small photo of the silver pendant"></div>
  <div class="corner-charm bl" role="img" aria-label="Small photo of the silver pendant"></div>
  <div class="corner-charm br" role="img" aria-label="Small photo of the silver pendant"></div>

  <h2 class="product-title">Crescent Loop Pendant</h2>

  <svg class="heart" viewBox="0 0 656 598" aria-hidden="true">
    <path d="M328 92 C300 30 240 0 170 0 C70 0 0 80 0 180 C0 330 160 450 328 598 C496 450 656 330 656 180 C656 80 586 0 486 0 C416 0 356 30 328 92 Z"/>
  </svg>

  <svg class="pendant" viewBox="0 0 370 520" role="img" aria-label="Photo of the silver pendant: three nested teardrop rings engraved with children's names around a tree of life, hung from a stone-set bail">
    <defs>
      <radialGradient id="silver" cx="45%" cy="45%" r="60%">
        <stop offset="0%" stop-color="#ffffff"/>
        <stop offset="100%" stop-color="#c3c9cc"/>
      </radialGradient>
    </defs>
    <rect x="160" y="0" width="50" height="110" rx="18" fill="url(#silver)"/>
    <path d="M185 90 C110 110 0 210 0 340 C0 440 80 520 185 520 C290 520 370 440 370 340 C370 210 260 110 185 90 Z" fill="url(#silver)"/>
  </svg>

  <p class="tagline">An expression of love</p>
</main>
</body>
</html>
```